Design some Business Cards for Coral Ridge

We need Business Cards Designed for Coral Ridge SARL
On the front Side we will have Company Name, Employee name, Position , email and 3d Barcode
On the Back Side we Will have Address and Website , Tel and Logo

We are open to other design options.

We will provide another files for our logo

```html
<!DOCTYPE html>
<html lang="en">
<head>
<meta charset="utf-8">
<title>Coral Ridge – Business Card</title>
<link rel="stylesheet" href="https://fonts.googleapis.com/css2?family=Montserrat:wght@400;500&family=Roboto+Condensed:ital,wght@0,400;0,500;0,700;1,400;1,700&display=swap">
<style>
  :root {
    --board: #c9c9c9;
    --card: #ffffff;
    --navy: #1f4466;
    --navy-text: #1f4466;
    --slate-dark: #2c343c;
    --slate-mid: #4b5560;
    --slate-light: #6c7680;
    --brand-blue: #5a8fc2;
    --white: #ffffff;
    --ink: #111111;
  }
  * { box-sizing: border-box; margin: 0; padding: 0; }
  html, body { width: 1200px; height: 1200px; overflow: hidden; }
  body {
    background: var(--board);
    position: relative;
    font-family: "Roboto Condensed", "Arial Narrow", sans-serif;
  }
  .side-label {
    position: absolute;
    font-family: "Roboto Condensed", sans-serif;
    font-style: italic;
    font-weight: 700;
    font-size: 54px;
    color: var(--ink);
    line-height: 1;
  }
  .side-label.front { left: 66px; top: 30px; }
  .side-label.back { left: 1004px; top: 1106px; }

  .card {
    position: absolute;
    background: var(--card);
    border-radius: 20px;
    overflow: hidden;
  }
  .card-front { left: 55px; top: 97px; width: 820px; height: 468px; }
  .card-back { left: 328px; top: 615px; width: 819px; height: 465px; }

  .abs { position: absolute; }

  /* Front */
  .employee-name {
    left: 58px; top: 62px;
    font-family: "Montserrat", sans-serif;
    font-size: 29px; font-weight: 400; letter-spacing: 1px;
    color: var(--navy-text);
  }
  .employee-role {
    left: 58px; top: 95px;
    font-size: 19px; font-weight: 500; color: var(--navy-text);
  }
  .contact-line {
    display: flex; align-items: center; gap: 8px;
    font-size: 20px; color: var(--navy-text);
  }
  .contact-line svg { width: 22px; height: 22px; flex: none; }
  .front-phone { left: 58px; top: 142px; }
  .info-band {
    left: 0; top: 235px; width: 820px; height: 180px;
    background: var(--navy);
  }
  .info-band .contact-line { color: var(--white); font-size: 20px; }
  .band-address { left: 52px; top: 18px; }
  .band-tel { left: 52px; top: 72px; }
  .band-fax { left: 52px; top: 103px; }
  .band-mail { left: 52px; top: 131px; }
  .band-web { left: 477px; top: 130px; }

  .brand-backer { left: 356px; top: 127px; width: 22px; height: 108px; background: var(--slate-light); }
  .brand-panel {
    left: 376px; top: 107px; width: 444px; height: 189px;
    background: linear-gradient(100deg, var(--slate-dark) 0%, var(--slate-mid) 70%, #59636d 100%);
    display: flex; align-items: center; justify-content: center; gap: 14px;
  }
  .brand-mark { width: 38px; height: 38px; background: var(--brand-blue); }
  .brand-name {
    font-family: "Roboto Condensed", sans-serif;
    font-weight: 400; font-size: 38px; letter-spacing: 2px;
    color: var(--brand-blue);
  }

  /* Back */
  .slogan-backer { left: 14px; top: 42px; width: 352px; height: 126px; background: var(--slate-light); }
  .slogan-panel {
    left: 0; top: 34px; width: 354px; height: 127px;
    background: linear-gradient(100deg, var(--slate-dark) 0%, var(--slate-mid) 100%);
  }
  .company-slogan {
    left: 36px; top: 42px;
    font-size: 19px; letter-spacing: 3px; color: var(--white);
  }
  .slogan-panel .brand-row {
    position: absolute; left: 34px; top: 58px;
    display: flex; align-items: center; gap: 12px;
  }
  .slogan-panel .brand-mark { width: 32px; height: 32px; }
  .slogan-panel .brand-name { font-size: 33px; }

  .address-block {
    font-size: 19px; line-height: 23px; font-weight: 500; color: var(--navy-text);
  }
  .addr-1 { left: 47px; top: 178px; }
  .addr-2 { left: 284px; top: 178px; }
  .addr-3 { left: 42px; top: 270px; }
  .addr-4 { left: 284px; top: 270px; }
  .back-web { left: 41px; top: 386px; font-size: 20px; font-weight: 500; color: var(--navy-text); }

  .services-panel {
    left: 521px; top: 0; width: 298px; height: 465px;
    background: var(--navy); color: var(--white);
  }
  .services-title { position: absolute; left: 32px; top: 30px; font-size: 19px; font-weight: 500; }
  .services-list { position: absolute; left: 55px; top: 74px; list-style: none; }
  .services-list li { font-style: italic; font-size: 19px; height: 45px; }
  .social-link { position: absolute; left: 32px; font-size: 19px; font-weight: 500; }
  .social-first { top: 340px; }
  .social-second { top: 386px; }
</style>
</head>
<body>
  <div class="side-label front">Front</div>

  <section class="card card-front">
    <div class="abs employee-name">JOHN DOE</div>
    <div class="abs employee-role">Vice President</div>
    <div class="abs contact-line front-phone">
      <svg viewBox="0 0 24 24" fill="none" stroke="currentColor" stroke-width="1.6"><path d="M5 3h4l2 5-3 2a12 12 0 0 0 6 6l2-3 5 2v4a2 2 0 0 1-2 2A17 17 0 0 1 3 5a2 2 0 0 1 2-2z"/></svg>
      <span>123-456-7890</span>
    </div>

    <div class="abs info-band">
      <div class="abs contact-line band-address">
        <svg viewBox="0 0 24 24" fill="none" stroke="currentColor" stroke-width="1.6"><path d="M12 21s-6-6.5-6-11a6 6 0 0 1 12 0c0 4.5-6 11-6 11z"/><circle cx="12" cy="10" r="2"/></svg>
        <span>Address</span>
      </div>
      <div class="abs contact-line band-tel">
        <svg viewBox="0 0 24 24" fill="none" stroke="currentColor" stroke-width="1.6"><rect x="4" y="3" width="16" height="18" rx="1"/><rect x="7" y="6" width="10" height="4"/><path d="M8 13h2M11 13h2M14 13h2M8 16h2M11 16h2M14 16h2"/></svg>
        <span>123-456-7890</span>
      </div>
      <div class="abs contact-line band-fax">
        <svg viewBox="0 0 24 24" fill="none" stroke="currentColor" stroke-width="1.6"><rect x="7" y="3" width="10" height="6"/><rect x="3" y="9" width="18" height="8" rx="1"/><rect x="7" y="14" width="10" height="7"/></svg>
        <span>02 41.628.305</span>
      </div>
      <div class="abs contact-line band-mail">
        <svg viewBox="0 0 24 24" fill="none" stroke="currentColor" stroke-width="1.6"><rect x="3" y="5" width="18" height="14"/><path d="M3 5l9 8 9-8"/></svg>
        <span>info@coralridge.com</span>
      </div>
      <div class="abs contact-line band-web">
        <svg viewBox="0 0 24 24" fill="none" stroke="currentColor" stroke-width="1.6"><circle cx="12" cy="12" r="9"/><path d="M3 12h18M12 3c3 3 3 15 0 18M12 3c-3 3-3 15 0 18"/></svg>
        <span>http://www.coralridge.com/</span>
      </div>
    </div>

    <div class="abs brand-backer"></div>
    <div class="abs brand-panel" role="img" aria-label="Coral Ridge name over a dark office photograph">
      <span class="brand-mark"></span>
      <span class="brand-name">CORAL RIDGE</span>
    </div>
  </section>

  <section class="card card-back">
    <div class="abs slogan-backer"></div>
    <div class="abs slogan-panel" role="img" aria-label="Coral Ridge name over a dark office photograph">
      <div class="brand-row">
        <span class="brand-mark"></span>
        <span class="brand-name">CORAL RIDGE</span>
      </div>
    </div>
    <div class="abs company-slogan">Company Slogan</div>

    <div class="abs address-block addr-1">Address 1 Line 1<br>Bldg. Name, Street Name<br>City and State, ZIP Code</div>
    <div class="abs address-block addr-2">Address 2 Line 1<br>Bldg. Name, Street Name<br>City and State, ZIP Code</div>
    <div class="abs address-block addr-3">Address 3 Line 1<br>Bldg. Name, Street Name<br>City and State, ZIP Code</div>
    <div class="abs address-block addr-4">Address 4 Line 1<br>Bldg. Name, Street Name<br>City and State, ZIP Code</div>
    <div class="abs back-web">http://www.coralridge.com/</div>

    <aside class="abs services-panel">
      <div class="services-title">Product and Services</div>
      <ul class="services-list">
        <li>Product and Services&nbsp; 1</li>
        <li>Product and Services&nbsp; 2</li>
        <li>Product and Services&nbsp; 3</li>
        <li>Product and Services&nbsp; 4</li>
        <li>Product and Services&nbsp; 5</li>
      </ul>
      <div class="social-link social-first">Linkhub Account</div>
      <div class="social-link social-second">Chirpline Account</div>
    </aside>
  </section>

  <div class="side-label back">Back</div>
</body>
</html>
```